Garden Maintenance business card

I need a business card design for my new business "Silver Birch Garden Co". I do garden maintenance including lawns, turf lawn, pruning, hedging, water systems, anything related to the garden really (dont think i need to include any of that except garden maintenance)

Reason: narrowed it down and just showing my business partners the designs, cheers

Industry/Entity Type

Business

Requirements
Must have
• Must Have:
- ABN: XX XXX XXX XXX
Mobile phone number 00 0000000
email address xxxx.xxxxxx@gmail.com
Owner Name Xxxx xxxxxx
title: garden specialist possibly under name or something sounding professional
logo which has been submitted both with a background and one without, feel free to choose whichever one you like
business name

```html
<!DOCTYPE html>
<html lang="en">
<head>
<meta charset="utf-8">
<title>Silver Birch Garden Co — Business Card</title>
<link rel="stylesheet" href="https://fonts.googleapis.com/css2?family=Bebas+Neue&family=Comfortaa:wght@400&display=swap">
<style>
  :root {
    --bg: #6e6e6e;
    --card-green: #66821e;
    --card-white: #ffffff;
    --olive-light: #b3ba55;
    --olive: #9aa83c;
    --ink-grey: #5f5f5f;
    --brand-white: #ffffff;
    --art-light: #e9e5d6;
    --art-mid: #cfc9b2;
    --art-leaf: #7fae5a;
  }
  * { margin: 0; padding: 0; box-sizing: border-box; }
  html, body { width: 1200px; height: 900px; overflow: hidden; }
  body { background: var(--bg); position: relative; }

  .card {
    position: absolute;
    left: 345px;
    width: 510px;
    height: 284px;
    overflow: hidden;
    box-shadow: 0 6px 14px rgba(0,0,0,0.35);
  }
  .card--front { top: 164px; background: var(--card-green); }
  .card--back  { top: 454px; background: var(--card-white); }

  .artwork {
    position: absolute;
    border-radius: 4px;
  }
  .card--front .artwork {
    right: 0; top: 48px; width: 135px; height: 210px;
    background: linear-gradient(180deg, rgba(40,70,20,0.55) 0%, var(--art-leaf) 40%, var(--art-light) 62%, var(--art-mid) 100%);
  }
  .card--back .artwork {
    left: 0; top: 48px; width: 135px; height: 206px;
    background: linear-gradient(180deg, rgba(40,70,20,0.45) 0%, var(--art-leaf) 38%, var(--art-light) 60%, var(--art-mid) 100%);
  }

  .brand {
    position: absolute;
    left: 26px;
    top: 198px;
  }
  .brand__name {
    font-family: "Comfortaa", sans-serif;
    font-weight: 400;
    font-size: 27px;
    color: var(--brand-white);
    line-height: 1;
    white-space: nowrap;
  }
  .brand__tagline {
    font-family: "Bebas Neue", sans-serif;
    font-size: 27px;
    letter-spacing: 3px;
    color: var(--olive-light);
    line-height: 1;
    margin-top: 2px;
  }

  .contact {
    position: absolute;
    left: 170px;
    top: 104px;
    font-family: "Bebas Neue", sans-serif;
  }
  .contact__name {
    font-size: 42px;
    color: var(--ink-grey);
    line-height: 1;
  }
  .contact__role {
    font-size: 18px;
    color: var(--olive);
    line-height: 1;
    margin-top: 1px;
  }
  .contact__list {
    margin-top: 26px;
    display: grid;
    grid-template-columns: 60px auto;
    row-gap: 2px;
    font-size: 19px;
    line-height: 1.1;
  }
  .contact__label { color: var(--olive); }
  .contact__value { color: var(--ink-grey); }
</style>
</head>
<body>
  <section class="card card--front">
    <div class="brand">
      <div class="brand__name">Silver Birch Garden Co</div>
      <div class="brand__tagline">Garden Specialist</div>
    </div>
    <div class="artwork" role="img" aria-label="Watercolour garden artwork area"></div>
  </section>

  <section class="card card--back">
    <div class="artwork" role="img" aria-label="Watercolour garden artwork area"></div>
    <div class="contact">
      <div class="contact__name">Alex Marlow</div>
      <div class="contact__role">Owner</div>
      <dl class="contact__list">
        <dt class="contact__label">Tel</dt><dd class="contact__value">555.01.23</dd>
        <dt class="contact__label">@</dt><dd class="contact__value">amarlow@example.com</dd>
        <dt class="contact__label">ABN</dt><dd class="contact__value">98765432100</dd>
      </dl>
    </div>
  </section>
</body>
</html>
```